Business Card for beauty technology startup

Design Glowra Business Card for a Beauty, based on the website identity and colors (https://www.glowra-example.com).
Glowra is a beauty tech startup that gathers helpful product info for beauty lovers and consumers (such as availability on stores, price range and product reviews) for makeup products. The card design must be young, colorful but clean, and very modern.

Target Market(s)

woman, 15-35

Industry/Entity Type

Cosmetics

Contact Information for Business Card

Full Name, address, phone

Font styles to use
Other font styles liked:
• Advent Pro

Colors
e34297
86cfc6
ffffff
5c5c5c
e8e8e8
e667a6
b2b2b2

Requirements
Must have
• One full colored side with a creative design and another with card info
• Use Color palette: #95C5C5 and/or #D38AA5
• Use fonts: Advent Pro
• Use website identity: https://www.glowra-example.com
Nice to have
• If needed extra font: Roboto

```html
<!DOCTYPE html>
<html lang="en">
<head>
<meta charset="utf-8">
<title>Glowra Business Card</title>
<link rel="stylesheet" href="https://fonts.googleapis.com/css2?family=Advent+Pro:wght@300;400;500;600&display=swap">
<style>
  :root {
    --backdrop: #ece8e6;
    --card-pink: #d487a4;
    --card-white: #ffffff;
    --ink-light: #ffffff;
    --ink-dark: #3a2a31;
    --accent-pink: #e34297;
    --rule-grey: #b2b2b2;
    --ghost: rgba(255, 255, 255, 0.14);
  }
  * { margin: 0; padding: 0; box-sizing: border-box; }
  html, body { width: 900px; height: 1200px; overflow: hidden; }
  body {
    position: relative;
    background: var(--backdrop);
    font-family: "Advent Pro", sans-serif;
  }
  .card {
    position: absolute;
    left: 107px;
    width: 688px;
    height: 403px;
    border-radius: 32px;
    overflow: hidden;
    box-shadow: 0 4px 14px rgba(0, 0, 0, 0.18);
  }
  .card--front { top: 145px; background: var(--card-pink); color: var(--ink-light); }
  .card--back { top: 628px; background: var(--card-white); color: var(--ink-dark); }

  .front__ghost-ring {
    position: absolute;
    left: 413px; top: 0;
    width: 290px; height: 290px;
    border: 6px solid var(--ghost);
    border-radius: 50%;
  }
  .front__mark {
    position: absolute;
    left: 292px; top: 116px;
    width: 86px; height: 86px;
    border: 2.5px solid var(--ink-light);
    border-radius: 50%;
  }
  .front__name {
    position: absolute;
    left: 0; right: 0; top: 236px;
    text-align: center;
    font-weight: 300;
    font-size: 46px;
    letter-spacing: 7px;
    line-height: 1;
  }
  .front__web {
    position: absolute;
    left: 0; right: 0; top: 339px;
    text-align: center;
    font-weight: 400;
    font-size: 19px;
    letter-spacing: 0.5px;
  }

  .back__mark {
    position: absolute;
    left: 164px; top: 115px;
    width: 86px; height: 86px;
    border: 2.5px solid var(--ink-dark);
    border-radius: 50%;
  }
  .back__brand {
    position: absolute;
    left: 284px; top: 132px;
    font-weight: 300;
    font-size: 56px;
    letter-spacing: 8px;
    line-height: 1;
  }
  .back__person {
    position: absolute;
    left: 0; right: 0; top: 220px;
    text-align: center;
    font-weight: 500;
    font-size: 30px;
    letter-spacing: 0.5px;
    line-height: 1;
  }
  .back__role {
    position: absolute;
    left: 0; right: 0; top: 254px;
    text-align: center;
    font-weight: 400;
    font-size: 16px;
    color: var(--accent-pink);
  }
  .back__rule {
    position: absolute;
    left: 206px; top: 282px;
    width: 276px; height: 1px;
    background: linear-gradient(to right, transparent, var(--rule-grey), transparent);
  }
  .back__contact {
    position: absolute;
    left: 0; right: 0; top: 292px;
    text-align: center;
    font-weight: 400;
    font-size: 16px;
    line-height: 24px;
  }
</style>
</head>
<body>
  <section class="card card--front" aria-label="Card front">
    <div class="front__ghost-ring"></div>
    <div class="front__mark"></div>
    <div class="front__name">GLOWRA</div>
    <div class="front__web">www.glowra-example.com</div>
  </section>

  <section class="card card--back" aria-label="Card back">
    <div class="back__mark"></div>
    <div class="back__brand">GLOWRA</div>
    <div class="back__person">Daniel Whitford</div>
    <div class="back__role">Managing Director</div>
    <div class="back__rule"></div>
    <div class="back__contact">
      <p>555.014.2731</p>
      <p>48 East 200 South, Maple Grove City 10482</p>
    </div>
  </section>
</body>
</html>
```